website design of a new wearable phone/gps called Brava Band

We are launching a product called Brava Band. Watch is a stand-alone cellular watch that allows anyone from kids to seniors to make phone calls by simply pushing one of four buttons on the watch. The SOS button connects you to a live team of emergency professionals that can patch you to a 911 operator. Two of the other buttons are programmable to dial any desired phone number. The fourth button (called the "Magic" button) connects you with a live team of personal assistants that can help you with anything you want, including transferring you to any number, making dinner reservations, answering trivia, finding movie times and anything else you can imagine. Our slogan is: "Always safe with Brava Band"
The built-in GPS functionality of the watch allows you to track the location of the watch at any time from the Brava Band website or the Brava Band app. You can also set up a perimeter around a specific area so that you can receive alerts when the watch travels outside of the "geofence".
There is a website that sells a similar product at http://www.quendo-kids.example - we like the look/feel and simplicity of this site. Now while we don't want a direct copy of this site, we would like a site that incorporates the simplicity of its layout and use of colors and images from the quendo-kids.example site.
We have included in the materials the Brava Band logo (in Adobe Illustrator).
We would like a site that shares the colors used for our logo. Please use stock images that you see fit to use for the mockup. We will be providing custom photographed images for the final site.
We would like to start first with the home page design, and when we select a winning designer, we would like for them to create the "About", "Technology", "Store" and "Support" pages.
For the home page, for now you can use the same content as they have on the quendo-kids.example site - ours will be different, but we are still working on creating the final copy that will go on the site.
We would like final deliverable code to be responsive (for mobile etc)
Any questions, let us know.

```html
<!DOCTYPE html>
<html lang="en">
<head>
<meta charset="utf-8">
<title>Brava Band – Always safe with Brava Band</title>
<link rel="stylesheet" href="https://fonts.googleapis.com/css2?family=Open+Sans:ital,wght@0,400;0,600;0,700;1,400&family=Roboto:wght@300;400;500;700&display=swap">
<style>
:root{
  --accent:#5cc3ea;
  --ink:#222428;
  --text:#4a4d52;
  --line:#e3e6e9;
  --band:#ececec;
  --pale:#f4fbfd;
  --footer:#232426;
  --white:#ffffff;
}
*{box-sizing:border-box;margin:0;padding:0}
html,body{width:1200px;height:2894px;overflow:hidden}
body{font-family:"Open Sans",Arial,sans-serif;color:var(--text);background:var(--white);position:relative}
section,header,footer{position:absolute;left:0;width:1200px}
.abs{position:absolute}

/* wordmark */
.brand-name{font-family:"Roboto",Arial,sans-serif;font-weight:500;color:var(--ink);font-size:38px;letter-spacing:.5px;line-height:1}
.brand-block{display:inline-block;text-align:right}
.brand-block .brand-name{font-size:27px;display:block}
.brand-sub{font-family:"Roboto",Arial,sans-serif;font-weight:300;font-size:23px;color:var(--text);letter-spacing:.5px;line-height:1;margin-top:6px;display:block}

/* header */
.site-header{top:0;height:120px;background:var(--white);border-top:4px solid #222;z-index:3}
.site-header .brand-name{position:absolute;left:100px;top:36px}
.main-nav{position:absolute;right:90px;top:50px;display:flex;gap:38px;font-size:14px;font-weight:600;color:var(--ink);letter-spacing:.3px}
.main-nav .active{color:var(--accent)}

/* hero */
.hero{top:120px;height:594px;z-index:2;background:linear-gradient(100deg,#555a60 0%,#3e4247 45%,#2c2f33 100%);clip-path:polygon(0 0,100% 0,100% 545px,50% 594px,0 545px)}
.hero-watch{left:270px;top:92px;width:222px;height:368px;border-radius:40px;background:linear-gradient(180deg,#6dcbf0 0%,#4fb9e6 100%)}
.kicker{font-family:"Roboto",Arial,sans-serif;font-weight:400;font-size:21px;letter-spacing:1.5px;color:#e7eaec}
.hero-title{font-family:"Open Sans",Arial,sans-serif;font-weight:700;font-size:33px;line-height:40px;color:var(--white);letter-spacing:.5px}
.hero-copy{font-size:14px;line-height:24px;color:#eef0f2}
.btn-light{display:inline-block;background:var(--white);color:var(--ink);font-size:12.5px;font-weight:700;letter-spacing:.6px;padding:12px 26px;border-radius:2px}
.arrow{width:40px;height:72px}

/* features band */
.features{top:665px;height:227px;background:var(--band);z-index:1}
.feature{display:flex;align-items:center;gap:14px;font-family:"Roboto",Arial,sans-serif;font-size:12.5px;letter-spacing:.6px;color:var(--ink);line-height:19px;text-transform:uppercase}
.icon-circle{width:50px;height:50px;border-radius:50%;background:var(--white);border:1px solid #dde0e3;display:flex;align-items:center;justify-content:center;flex:none}

/* details */
.details{top:892px;height:633px;background:var(--pale)}
.details-copy{left:100px;top:160px;width:610px;font-size:12.5px;line-height:23px;color:var(--ink)}
.detail-grid{left:100px;top:253px;width:598px;display:grid;grid-template-columns:repeat(3,1fr);grid-template-rows:175px 140px;row-gap:12px}
.detail-cell{display:flex;flex-direction:column;align-items:center;justify-content:flex-start;padding-top:14px;border-right:1px solid var(--line);border-left:1px solid var(--line);margin-left:-1px}
.detail-cell .icon-circle{width:64px;height:64px;border-color:#d9e7ec}
.detail-label{margin-top:22px;font-size:13.5px;font-weight:600;color:var(--ink);letter-spacing:.3px}
.device-shot{left:768px;top:150px;width:312px;height:400px;border-radius:34px;background:linear-gradient(160deg,#3fb6e6 0%,#e9f3f7 45%,#2b2d31 100%)}

/* dark promo */
.promo{top:1525px;height:488px;background:linear-gradient(90deg,#141517 0%,#1e2022 40%,#3d4145 75%,#6f7479 100%)}
.promo-copy{left:116px;top:115px;width:470px}
.promo .hero-title{font-size:34px;line-height:41px}
.store-badge{width:162px;height:44px;border:1.5px solid #9a9ea3;border-radius:6px;background:#111}

/* testimonials */
.testimonials{top:2013px;height:380px;background:linear-gradient(180deg,#7fd7f2 0%,#4fbde7 100%);color:var(--white);text-align:center}
.section-title{font-family:"Roboto",Arial,sans-serif;font-size:28px;font-weight:300;letter-spacing:.5px}
.section-title b{font-weight:700}
.quote{left:232px;top:118px;width:762px;font-style:italic;font-size:12.5px;line-height:19px;color:#f2fbff;text-align:center}
.qmark{font-family:Georgia,serif;font-size:46px;font-weight:700;line-height:1}
.avatar{left:502px;top:210px;width:108px;height:108px;border-radius:50%;border:5px solid var(--white);background:linear-gradient(160deg,#c9b8a6,#8a7563)}
.person{left:633px;top:232px;text-align:left}
.person-name{font-size:17px;font-weight:600}
.person-role{font-size:12.5px;color:#e6f7fd;margin-top:6px}

/* clients */
.clients{top:2393px;height:187px;background:var(--white)}
.client-box{top:54px;width:180px;height:78px;border:4px solid #d4d6d8;display:flex;align-items:center;justify-content:center;gap:10px;font-family:"Open Sans",Arial,sans-serif;font-weight:600;font-size:20px;color:#2d2f33}
.client-dot{width:18px;height:18px;background:#2d2f33}
.client-dot.round{border-radius:50%}

/* footer */
.site-footer{top:2580px;height:314px;background:var(--footer);color:#b9bcc0}
.foot-col{top:60px;width:230px}
.foot-col h4{font-size:15px;font-weight:700;color:var(--white);letter-spacing:.3px;margin-bottom:20px}
.foot-col li{list-style:none;font-size:12.5px;line-height:26.5px;color:#c3c6ca}
.foot-divider{top:55px;width:1px;height:190px;background:#34363a}
.news-copy{font-size:12.5px;line-height:21px;color:#c3c6ca}
.news-input{width:228px;height:40px;background:var(--white);margin-top:18px;padding:12px;font-size:11px;color:#a0a3a7}
.news-btn{display:inline-block;width:116px;height:39px;margin-top:11px;background:var(--accent);color:var(--white);font-size:11.5px;line-height:39px;text-align:center}
.copyright{left:100px;top:252px;font-size:12px;color:#a9acb0}
</style>
</head>
<body>

<header class="site-header">
  <span class="brand-name">BRAVA BAND</span>
  <nav class="main-nav">
    <span class="active">HOME</span><span>ABOUT US</span><span>OUR TEAM</span><span>TECHNOLOGY</span><span>STORE</span><span>SUPPORT</span>
  </nav>
</header>

<section class="hero" role="img" aria-label="Photo of a hand wearing a smart watch, blurred dark background">
  <div class="abs hero-watch" role="img" aria-label="Light blue smart watch showing an activity screen"></div>
  <svg class="abs arrow" style="left:70px;top:225px" viewBox="0 0 40 72"><polyline points="34,4 6,36 34,68" fill="none" stroke="#c9ccd0" stroke-width="2"/></svg>
  <svg class="abs arrow" style="left:1092px;top:225px" viewBox="0 0 40 72"><polyline points="6,4 34,36 6,68" fill="none" stroke="#c9ccd0" stroke-width="2"/></svg>
  <div class="abs" style="left:585px;top:165px;width:460px">
    <div class="kicker">MADE FOR EVERY THING</div>
    <h1 class="hero-title" style="margin-top:12px">ALLWAYS SAFE &amp;<br>WITH BRAVA BAND</h1>
    <p class="hero-copy" style="margin-top:14px">Lorem ipsum dolor sit amet, consectetur adipiscing elit, sed doquis nos eiusmod tempor incididunt ut dolore magna aliqua.</p>
    <div style="margin-top:22px;display:flex;gap:14px">
      <span class="btn-light">WATCH THE VIDEO</span><span class="btn-light">LEARN MORE</span>
    </div>
  </div>
</section>

<section class="features">
  <div class="abs brand-block" style="left:100px;top:108px">
    <span class="brand-name">BRAVA BAND</span>
    <span class="brand-sub">FEATURES</span>
  </div>
  <div class="abs feature" style="left:332px;top:110px">
    <span class="icon-circle"><svg width="22" height="22" viewBox="0 0 24 24"><path d="M6.6 10.8a15 15 0 0 0 6.6 6.6l2.2-2.2c.3-.3.7-.4 1-.2 1.1.4 2.3.6 3.6.6.6 0 1 .4 1 1V20c0 .6-.4 1-1 1A17 17 0 0 1 3 4c0-.6.4-1 1-1h3.5c.6 0 1 .4 1 1 0 1.2.2 2.4.6 3.6.1.3 0 .7-.2 1z" fill="none" stroke="var(--accent)" stroke-width="1.6"/></svg></span>
    <span>VOICE<br>CALLINGS</span>
  </div>
  <div class="abs feature" style="left:531px;top:110px">
    <span class="icon-circle"><svg width="22" height="22" viewBox="0 0 24 24"><path d="M12 2a7 7 0 0 0-7 7c0 5 7 13 7 13s7-8 7-13a7 7 0 0 0-7-7z" fill="var(--accent)"/><circle cx="12" cy="9" r="2.6" fill="#fff"/></svg></span>
    <span>SMART<br>LOCATOR</span>
  </div>
  <div class="abs feature" style="left:730px;top:110px">
    <span class="icon-circle"><svg width="22" height="22" viewBox="0 0 24 24"><rect x="3" y="5" width="18" height="14" fill="none" stroke="var(--accent)" stroke-width="1.6"/><path d="M12 8v8M8 12h8" stroke="var(--accent)" stroke-width="1.6"/></svg></span>
    <span>QUICK<br>EMERGENCY</span>
  </div>
  <div class="abs feature" style="left:926px;top:110px">
    <span class="icon-circle"><svg width="22" height="22" viewBox="0 0 24 24"><rect x="3" y="5" width="16" height="15" fill="none" stroke="var(--accent)" stroke-width="1.6"/><path d="M3 9h16M7 3v4M15 3v4" stroke="var(--accent)" stroke-width="1.6"/><circle cx="17" cy="17" r="4.5" fill="#fff" stroke="var(--accent)" stroke-width="1.6"/><path d="M17 15v2.2h1.6" stroke="var(--accent)" stroke-width="1.3" fill="none"/></svg></span>
    <span>TIME AND<br>DATE</span>
  </div>
</section>

<section class="details">
  <div class="abs brand-block" style="left:100px;top:68px">
    <span class="brand-name">BRAVA BAND</span>
    <span class="brand-sub">IN DETAILS</span>
  </div>
  <p class="abs details-copy">Lorem ipsum dolor sit amet, consectetur adipiscing elit, sed do eiusmod tempor incididunt ut labore et dolore magna aliqua. Ut enim ad minim veniam, quis nostrud exercitation ullamco laboris nisi ut aliquip ex ea commodo consequat. Duis aute irure dolor in reprehenderit in voluptate cillum dolore .</p>
  <div class="abs detail-grid">
    <div class="detail-cell"><span class="icon-circle"><svg width="24" height="24" viewBox="0 0 24 24"><path d="M6.6 10.8a15 15 0 0 0 6.6 6.6l2.2-2.2c.3-.3.7-.4 1-.2 1.1.4 2.3.6 3.6.6.6 0 1 .4 1 1V20c0 .6-.4 1-1 1A17 17 0 0 1 3 4c0-.6.4-1 1-1h3.5c.6 0 1 .4 1 1 0 1.2.2 2.4.6 3.6.1.3 0 .7-.2 1z" fill="none" stroke="var(--accent)" stroke-width="1.6"/></svg></span><span class="detail-label">VOICE CALLING</span></div>
    <div class="detail-cell"><span class="icon-circle"><svg width="26" height="24" viewBox="0 0 26 24"><rect x="2" y="4" width="22" height="16" fill="none" stroke="var(--accent)" stroke-width="1.6"/><path d="M13 7v10M8 12h10" stroke="var(--accent)" stroke-width="1.8"/></svg></span><span class="detail-label">EMERGENCY</span></div>
    <div class="detail-cell"><span class="icon-circle"><svg width="22" height="26" viewBox="0 0 22 26"><rect x="3" y="4" width="16" height="20" fill="none" stroke="var(--accent)" stroke-width="1.6"/><rect x="7" y="2" width="8" height="4" fill="#fff" stroke="var(--accent)" stroke-width="1.4"/><path d="M7 11h8M7 15h8M7 19h6" stroke="var(--accent)" stroke-width="1.4"/></svg></span><span class="detail-label">RESERVATIONS</span></div>
    <div class="detail-cell"><span class="icon-circle"><svg width="22" height="24" viewBox="0 0 24 24"><path d="M12 2a7 7 0 0 0-7 7c0 5 7 13 7 13s7-8 7-13a7 7 0 0 0-7-7z" fill="var(--accent)"/><circle cx="12" cy="9" r="2.6" fill="#fff"/></svg></span><span class="detail-label">SMART LOCATOR</span></div>
    <div class="detail-cell"><span class="icon-circle"><svg width="28" height="22" viewBox="0 0 28 22"><rect x="2" y="3" width="24" height="16" fill="var(--accent)"/><polyline points="2,3 14,12 26,3" fill="none" stroke="#fff" stroke-width="1.6"/></svg></span><span class="detail-label">MESSAGING</span></div>
    <div class="detail-cell"><span class="icon-circle"><svg width="24" height="26" viewBox="0 0 24 26"><circle cx="12" cy="8" r="5.5" fill="var(--accent)"/><path d="M2 25c0-6 4.5-10 10-10s10 4 10 10z" fill="var(--accent)"/></svg></span><span class="detail-label">CONNECT ASSISTANTS</span></div>
  </div>
  <div class="abs device-shot" role="img" aria-label="Blue smartphone showing the Brava Band tracking app next to a black smart watch"></div>
</section>

<section class="promo" role="img" aria-label="Close-up photo of a smart watch with app icons on a dark desk">
  <div class="abs promo-copy">
    <div class="kicker">MADE FOR EVERY THING</div>
    <h2 class="hero-title" style="margin-top:6px">ALL INFORMATION &amp;<br>IMPORTANT FEATURES</h2>
    <p class="hero-copy" style="margin-top:14px">Lorem ipsum dolor sit amet, consectetur adipiscing elit, sed doquis nos eiusmod tempor incididunt ut dolore magna aliqua.</p>
    <div class="store-badge" style="margin-top:30px" aria-label="App store badge"></div>
  </div>
</section>

<section class="testimonials">
  <h2 class="abs section-title" style="left:0;width:1200px;top:60px"><b>CLIENT</b> TESTIMONIALS</h2>
  <svg class="abs arrow" style="left:82px;top:150px" viewBox="0 0 40 72"><polyline points="34,4 6,36 34,68" fill="none" stroke="#e8f8fe" stroke-width="2"/></svg>
  <svg class="abs arrow" style="left:1078px;top:150px" viewBox="0 0 40 72"><polyline points="6,4 34,36 6,68" fill="none" stroke="#e8f8fe" stroke-width="2"/></svg>
  <span class="abs qmark" style="left:205px;top:100px">&ldquo;</span>
  <p class="abs quote">Sed ut perspiciatis unde omnis iste natus error sit voluptatem accusantium doloremque laudantium, totam rem aperiam, eaque ipsa quae ab illo inventore veritatis et quasi architecto beatae vitae dicta sunt explicabo. Nemo enim ipsam voluptatem quia voluptas sit aspernatur aut odit aut fugit, sed quia consequuntur magni dolores eos qui ratione</p>
  <span class="abs qmark" style="left:930px;top:160px">&rdquo;</span>
  <div class="abs avatar" role="img" aria-label="Portrait photo of the client"></div>
  <div class="abs person"><div class="person-name">John Doe</div><div class="person-role">Manager</div></div>
</section>

<section class="clients">
  <div class="abs brand-block" style="left:100px;top:64px">
    <span class="brand-name">BRAVA BAND</span>
    <span class="brand-sub">CLIENTS</span>
  </div>
  <div class="abs client-box" style="left:330px"><span class="client-dot round"></span>Dolorsit</div>
  <div class="abs client-box" style="left:531px"><span class="client-dot"></span>Northgrid</div>
  <div class="abs client-box" style="left:730px"><span class="client-dot"></span>Pinecraft</div>
  <div class="abs client-box" style="left:932px"><span class="client-dot round"></span>Layoutbear</div>
</section>

<footer class="site-footer">
  <div class="abs foot-col" style="left:100px"><h4>INFORMATION</h4><ul><li>Home</li><li>About us</li><li>Team</li><li>Technology</li><li>Support</li></ul></div>
  <div class="abs foot-divider" style="left:322px"></div>
  <div class="abs foot-col" style="left:349px"><h4>SUPPORT LINKS</h4><ul><li>Terms of Use</li><li>Privacy Policy</li><li>Contact</li></ul></div>
  <div class="abs foot-divider" style="left:571px"></div>
  <div class="abs foot-col" style="left:598px"><h4>SOCIAL LINKS</h4><ul><li>Friendline</li><li>Chirpcast</li><li>Workweb</li><li>Circlespace</li><li>Clipstream</li></ul></div>
  <div class="abs foot-divider" style="left:820px"></div>
  <div class="abs foot-col" style="left:849px;width:270px">
    <h4>NEWSLETTER SIGN UP</h4>
    <p class="news-copy">Lorem ipsum dolor sit amet, consectetur adipi-scing elit eiusmod tempor</p>
    <div class="news-input">Email Address ...</div>
    <span class="news-btn">SUBSCRIBE</span>
  </div>
  <p class="abs copyright">Copyright © 2016 Brava Band All rights reserved.</p>
</footer>

</body>
</html>
```